BUSINESS CARD - HALVERDINE RURAL SERVICES

I would like to create a business card for my fertilizer spreading business. I would like to incorporate my existing logo and also a description of the services offered. The business card will be given to farmers so must be kept simple but effective. It will also be left in stores so much also be eye catching in order to stand out from other cards.

Target Market(s)

FARMERS

Requirements
Must have
• FRONT OF CARD = EXISTING LOGO + "CUSTOMISED SPREADING" below the logo

REAR Of CARD = SERVICES OFFERED AND CONTACT DETAILS

- Bulk fertilizer including Lime, Gypsum, Manure & Compost
- Granular fertilizer including Single Super, Urea, Granosul, & Custom Blends
- Modern equipment - Autosteer & Variable Rate Capable
- Friendly & Reliable Service
- Contact Gus: 0471 502 318
Nice to have
• utilize same color scheme as existing logo

```html
<!DOCTYPE html>
<html lang="en">
<head>
<meta charset="utf-8">
<title>Halverdine Rural Services – Business Card</title>
<link href="https://fonts.googleapis.com/css2?family=Montserrat:wght@400;500;700&family=Crimson+Text:wght@700&display=swap" rel="stylesheet">
<style>
  :root {
    --ink-grey: #5a5a5c;
    --card-grey: #545457;
    --accent-orange: #f0922a;
    --paper: #ffffff;
    --backdrop: #e9e7e4;
    --emboss: rgba(255,255,255,0.10);
  }
  html, body {
    margin: 0;
    width: 1200px;
    height: 1200px;
    overflow: hidden;
    background: var(--backdrop);
    font-family: "Montserrat", Arial, sans-serif;
  }
  .canvas {
    position: relative;
    width: 1200px;
    height: 1200px;
  }
  .card {
    position: absolute;
    left: 150px;
    width: 900px;
    height: 514px;
    border-radius: 30px;
    overflow: hidden;
    box-shadow: 0 10px 30px rgba(0,0,0,0.18);
  }
  /* Front */
  .card-front {
    top: 46px;
    background: var(--paper);
    text-align: center;
  }
  .front-mark {
    position: absolute;
    left: 377px;
    top: 118px;
  }
  .front-name {
    position: absolute;
    left: 0; right: 0;
    top: 276px;
    margin: 0;
    font-weight: 700;
    font-size: 25px;
    letter-spacing: -0.3px;
    color: var(--ink-grey);
  }
  .front-tagline {
    position: absolute;
    left: 0; right: 0;
    top: 330px;
    margin: 0;
    font-weight: 400;
    font-size: 20px;
    letter-spacing: 2px;
    color: var(--ink-grey);
  }
  .front-phone {
    position: absolute;
    left: 0; right: 0;
    top: 362px;
    margin: 0;
    font-family: "Crimson Text", Georgia, serif;
    font-weight: 700;
    font-size: 30px;
    color: var(--accent-orange);
  }
  /* Back */
  .card-back {
    top: 640px;
    background: var(--card-grey);
    color: var(--paper);
  }
  .back-deco {
    position: absolute;
    left: 416px;
    top: 26px;
  }
  .back-name {
    position: absolute;
    left: 38px;
    top: 58px;
    margin: 0;
    font-weight: 700;
    font-size: 29px;
    letter-spacing: -0.4px;
  }
  .back-tagline {
    position: absolute;
    left: 38px;
    top: 130px;
    margin: 0;
    font-weight: 400;
    font-size: 18px;
    letter-spacing: 6px;
  }
  .service-list {
    position: absolute;
    left: 38px;
    top: 212px;
    margin: 0;
    padding: 0;
    list-style: none;
    font-size: 17px;
    line-height: 25px;
  }
  .service-list li {
    position: relative;
    padding-left: 24px;
    margin-bottom: 25px;
  }
  .service-list li::before {
    content: "";
    position: absolute;
    left: 2px;
    top: 9px;
    width: 8px;
    height: 8px;
    border-radius: 50%;
    background: var(--paper);
  }
</style>
</head>
<body>
<main class="canvas">
  <section class="card card-front" aria-label="Front of card">
    <svg class="front-mark" width="146" height="146" viewBox="0 0 146 146" aria-hidden="true">
      <circle cx="73" cy="73" r="70" fill="var(--ink-grey)"/>
    </svg>
    <h1 class="front-name">Halverdine Rural Services</h1>
    <p class="front-tagline">CUSTOMISED SPREADING</p>
    <p class="front-phone">Ph. 0471 502 318</p>
  </section>

  <section class="card card-back" aria-label="Back of card">
    <svg class="back-deco" width="460" height="460" viewBox="0 0 460 460" aria-hidden="true">
      <circle cx="230" cy="230" r="225" fill="none" stroke="var(--emboss)" stroke-width="4"/>
    </svg>
    <h2 class="back-name">Halverdine Rural Services</h2>
    <p class="back-tagline">CUSTOMISED SPREADING</p>
    <ul class="service-list">
      <li>Bulk fertilizer including Lime,<br>Gypsum, Manure &amp; Compost</li>
      <li>Granular fertilizer including Single<br>Super, Urea, Granosul, &amp; Custom Blends</li>
      <li>Modern equipment -<br>Autosteer &amp; Variable Rate Capable</li>
      <li>Friendly &amp; Reliable Service</li>
    </ul>
  </section>
</main>
</body>
</html>
```